Lanternfield Drinks business cards

We need a business card design for our new logo. The company is modern, progressive, professional, yet approachable. The key products are ready to drink bottles and cans of coffee based beverages.
These cards will be a critical part of the first impression made by our sales organization, business development team, and all external facing personnel.
Card can be a vertical or horizontal orientation.

Target Market(s)

Customers, suppliers, business partners

Industry/Entity Type

Business

Contact Information for Business Card

Business cards should feature Company Name and Logo.

Font styles to use
Serif

Colors

Designer to choose colors to be used in the design.

Requirements
Must have
• Strong readability of Name, phone #, mobile number and email address.
• Job title, website url, Street Address, and other details can be secondary level readability.
Nice to have
• High impact, simplistic quality design.
• Ok to utilize the 'H in the box' separate from the company name

```html
<!DOCTYPE html>
<html lang="en">
<head>
<meta charset="utf-8">
<title>Lanternfield Drinks – Business Cards</title>
<link rel="stylesheet" href="https://fonts.googleapis.com/css2?family=Lato:wght@400;700&family=Libre+Baskerville:wght@700&display=swap">
<style>
  :root {
    --backdrop: #8c8c8c;
    --card-light: #ffffff;
    --card-dark: #000000;
    --brand-orange: #f15a29;
    --brand-amber: #f7941d;
    --ink: #222222;
    --rule: #c8c8c8;
  }
  html, body {
    margin: 0;
    width: 1200px;
    height: 900px;
    overflow: hidden;
    background: var(--backdrop);
  }
  .canvas {
    position: relative;
    width: 1200px;
    height: 900px;
  }
  .card {
    position: absolute;
    top: 170px;
    width: 347px;
    height: 560px;
    box-shadow: 3px 3px 5px rgba(0,0,0,0.45);
  }
  .card--front { left: 259px; background: var(--card-light); }
  .card--back  { left: 631px; background: var(--card-dark); }

  /* Front card */
  .brand-block {
    position: absolute;
    top: 40px;
    left: 0;
    width: 100%;
    text-align: center;
  }
  .brand-square {
    display: block;
    margin: 0 auto 22px;
    width: 52px;
    height: 52px;
    border: 7px solid var(--brand-orange);
    box-sizing: border-box;
  }
  .brand-name {
    font-family: "Libre Baskerville", Georgia, serif;
    font-weight: 700;
    font-size: 22px;
    line-height: 1.25;
    color: var(--brand-orange);
    margin: 0;
  }
  .person {
    position: absolute;
    top: 310px;
    left: 0;
    width: 100%;
    text-align: center;
    font-family: "Lato", Arial, sans-serif;
  }
  .person__name {
    margin: 0;
    font-weight: 700;
    font-size: 23px;
    color: var(--brand-orange);
    letter-spacing: 0.2px;
  }
  .person__title {
    margin: 2px 0 0;
    font-size: 16px;
    color: var(--brand-amber);
  }
  .divider {
    width: 200px;
    height: 1px;
    background: var(--rule);
    margin: 12px auto;
    border: 0;
  }
  .contact-list {
    list-style: none;
    margin: 0;
    padding: 0;
    font-size: 16px;
    line-height: 19.5px;
    color: var(--ink);
  }
  .contact-list .label { color: var(--brand-orange); }
  .address {
    font-style: normal;
    font-size: 16px;
    line-height: 20px;
    color: var(--ink);
  }

  /* Back card */
  .back-square {
    position: absolute;
    left: 53px;
    top: 214px;
    width: 133px;
    height: 133px;
    border: 7px solid var(--brand-orange);
    box-sizing: border-box;
  }
  .wordmark {
    position: absolute;
    left: 237px;
    top: 280px;
    width: 460px;
    margin: 0;
    transform: translate(-50%, -50%) rotate(-90deg);
    text-align: center;
    white-space: nowrap;
    font-family: "Libre Baskerville", Georgia, serif;
    font-weight: 700;
    font-size: 33px;
    letter-spacing: 1px;
    color: var(--brand-orange);
  }
  .accent-rule {
    position: absolute;
    left: 283px;
    top: 52px;
    width: 3px;
    height: 456px;
    background: var(--brand-amber);
  }
</style>
</head>
<body>
<main class="canvas">
  <section class="card card--front" aria-label="Business card front">
    <div class="brand-block">
      <span class="brand-square"></span>
      <p class="brand-name">Lanternfield<br>Drinks</p>
    </div>
    <div class="person">
      <h1 class="person__name">LORUM SMITH</h1>
      <p class="person__title">MANAGING DIRECTOR</p>
      <hr class="divider">
      <ul class="contact-list">
        <li><span class="label">P</span>: 888 555 4433</li>
        <li><span class="label">M</span>: 888 444 0000</li>
        <li><span class="label">E</span>: info@webname.com</li>
        <li><span class="label">W</span>: www.webname.com</li>
      </ul>
      <hr class="divider">
      <address class="address">421, Address line here,<br>Dummy Code, 45452<br>Country Name</address>
    </div>
  </section>

  <section class="card card--back" aria-label="Business card back">
    <span class="back-square"></span>
    <p class="wordmark">LANTERNFIELD DRINKS</p>
    <span class="accent-rule"></span>
  </section>
</main>
</body>
</html>
```